High-end residential home builder needs a business card design

We need a new business card design for a small residential construction company based in Boise, Idaho. We specialize in building custom high-end homes and remodels, with a focus on great design and craftsmanship.

We would like to use our current logo, but open to new color suggestions.
Just looking for a clean, sharp, modern design that looks high-end.

Target Market(s)

Upscale clientele

Industry/Entity Type

Contractor

Contact Information for Business Card

Company: Stonefield Custom Builders
Name: Marcus Tilley
Phone number: 208 367 4120
Email: MarcusTilleySCB@mailbox-example.com
Website: Stonefieldcustombuilders-example.com

Font styles to use
Serif
Sans Serif

Requirements
Must have
• Company Logo
Company name
My name
My phone number
My email
Company website
Nice to have
• I have attached a few photos of cards that I really like.

```html
<!DOCTYPE html>
<html lang="en">
<head>
<meta charset="utf-8">
<title>Stonefield Custom Builders – Business Card</title>
<link href="https://fonts.googleapis.com/css2?family=Roboto:wght@400;500;700&display=swap" rel="stylesheet">
<style>
  :root {
    --backdrop: #e5e1db;
    --card-dark: #3b3b3b;
    --card-light: #fbfbfa;
    --ink-light: #ffffff;
    --ink-soft: #e6e6e6;
    --ink-brand: #3a2a22;
  }
  * { box-sizing: border-box; margin: 0; padding: 0; }
  html, body {
    width: 1200px; height: 800px; overflow: hidden;
    background: var(--backdrop);
    font-family: "Roboto", Arial, sans-serif;
  }
  .canvas { position: relative; width: 1200px; height: 800px; }
  .card {
    position: absolute; top: 264px;
    width: 410px; height: 244px;
    overflow: hidden;
  }
  .card--front { left: 130px; background: var(--card-dark); color: var(--ink-light); }
  .card--back { left: 660px; background: var(--card-light); }

  .front-mark {
    position: absolute; left: 66px; top: 84px;
    width: 76px; height: 76px;
    border: 2px solid var(--ink-light);
  }
  .holder {
    position: absolute; left: 200px; top: 56px;
    white-space: nowrap;
  }
  .holder__name { font-size: 22px; font-weight: 700; letter-spacing: 0.2px; line-height: 1.2; }
  .holder__company { font-size: 13px; font-weight: 400; color: var(--ink-soft); margin-top: 5px; }

  .contact {
    position: absolute; left: 200px; top: 134px;
    list-style: none; font-size: 10px; color: var(--ink-soft);
    white-space: nowrap;
  }
  .contact__item { display: flex; align-items: center; height: 17px; line-height: 17px; }
  .contact__icon { width: 10px; height: 10px; margin-right: 6px; fill: var(--ink-light); flex: none; }

  .brand {
    position: absolute; left: 0; right: 0; top: 62px;
    display: flex; flex-direction: column; align-items: center;
  }
  .brand__square {
    width: 70px; height: 70px;
    border: 2px solid var(--ink-brand);
  }
  .brand__name {
    margin-top: 16px;
    font-size: 13px; font-weight: 700; letter-spacing: 1.6px;
    text-transform: uppercase; color: var(--ink-brand);
    text-align: center; line-height: 1.45;
    white-space: nowrap;
  }
</style>
</head>
<body>
<main class="canvas">
  <section class="card card--front" aria-label="Business card front">
    <div class="front-mark"></div>
    <div class="holder">
      <h1 class="holder__name">Marcus Tilley</h1>
      <p class="holder__company">Stonefield Custom Builders</p>
    </div>
    <ul class="contact">
      <li class="contact__item">
        <svg class="contact__icon" viewBox="0 0 10 10"><rect x="0" y="0" width="10" height="10" rx="2"/><path d="M3 2.2l1 1.6-.7.7c.4.9 1.1 1.6 2 2l.7-.7 1.6 1-.6 1.2C4.6 7.8 2.2 5.4 2 3z" fill="#3b3b3b"/></svg>
        208 367 4120
      </li>
      <li class="contact__item">
        <svg class="contact__icon" viewBox="0 0 10 10"><path d="M0 2h10v6H0z"/><path d="M0 2l5 3.4L10 2" fill="none" stroke="#3b3b3b" stroke-width="1"/></svg>
        MarcusTilleySCB@mailbox-example.com
      </li>
      <li class="contact__item">
        <svg class="contact__icon" viewBox="0 0 10 10"><circle cx="5" cy="5" r="4.2" fill="none" stroke="#fff" stroke-width="1.2"/><circle cx="5" cy="5" r="1.6"/></svg>
        Stonefieldcustombuilders-example.com
      </li>
    </ul>
  </section>

  <section class="card card--back" aria-label="Business card back">
    <div class="brand">
      <div class="brand__square"></div>
      <p class="brand__name">Stonefield<br>Custom Builders</p>
    </div>
  </section>
</main>
</body>
</html>
```